design 3 a5 leaflets for tradesmen such as plumbers

I am looking for 3 flyers to be made for advertising painters and tradesmen. They are the type that have 10 - 12 tear away phone numbers.
I want 3 designs so that i can out compete the competition varnell tosk style. The winners will design 3 they don't need to be top class as the competition are generally home made. there will be three winners please use the phone numbers in the upload i gave you but advertise plumber on one leaflet and electrician saying local man ,competitive rates etc etc

```html
<!DOCTYPE html>
<html lang="en">
<head>
<meta charset="utf-8">
<title>Free Tradesperson Recommendation Service – Plumber</title>
<link rel="stylesheet" href="https://fonts.googleapis.com/css2?family=Archivo+Black&family=Montserrat:wght@500;700;800&family=Playfair+Display:ital,wght@1,700&display=swap">
<style>
  :root {
    --navy: #1b1f4b;
    --yellow: #ffe600;
    --sky: #2aa7df;
    --ink: #111111;
    --paper: #ffffff;
    --figure-main: #c8a27a;
    --figure-alt: #7fa6d6;
  }
  * { box-sizing: border-box; margin: 0; padding: 0; }
  html, body { width: 849px; height: 1200px; overflow: hidden; background: var(--paper); }
  .leaflet {
    position: relative;
    width: 849px;
    height: 1200px;
    background: var(--paper);
    font-family: "Montserrat", Arial, sans-serif;
    color: var(--navy);
    overflow: hidden;
  }
  .brand {
    position: absolute;
    top: 150px; left: 0; width: 100%;
    text-align: center;
    font-family: "Montserrat", Arial, sans-serif;
    font-weight: 500;
    font-size: 40px;
    letter-spacing: 2px;
    color: var(--sky);
  }
  .badge-free {
    position: absolute;
    left: 28px; top: 264px;
    width: 152px; height: 52px;
    background: var(--yellow);
    color: var(--ink);
    font-family: "Archivo Black", Arial, sans-serif;
    font-size: 40px;
    line-height: 52px;
    text-align: center;
  }
  .headline {
    position: absolute;
    top: 318px; left: 0; width: 100%;
    text-align: center;
    font-family: "Archivo Black", Arial, sans-serif;
    font-size: 86px;
    line-height: 1.1;
    color: var(--navy);
    text-shadow: 0 0 3px var(--yellow), 0 0 6px var(--yellow), 0 0 10px var(--yellow);
  }
  .subheadline {
    position: absolute;
    top: 428px; left: 0; width: 100%;
    text-align: center;
    font-family: "Playfair Display", Georgia, serif;
    font-style: italic;
    font-weight: 700;
    font-size: 50px;
    color: var(--ink);
    text-shadow: 0 0 4px var(--yellow), 0 0 8px var(--yellow);
  }
  .trade-range {
    position: absolute;
    left: 44px; top: 522px;
    font-weight: 800;
    font-size: 32px;
    color: var(--navy);
  }
  .trade-panel {
    position: absolute;
    left: 36px; top: 590px;
    width: 504px; height: 86px;
    background: var(--navy);
    color: var(--yellow);
    font-family: "Archivo Black", Arial, sans-serif;
    font-size: 66px;
    line-height: 86px;
    padding-left: 32px;
  }
  .call-prompt {
    position: absolute;
    left: 36px; top: 690px;
    height: 28px;
    padding: 0 8px;
    background: var(--yellow);
    font-family: "Playfair Display", Georgia, serif;
    font-style: italic;
    font-weight: 700;
    font-size: 22px;
    line-height: 28px;
    color: var(--ink);
    display: flex; align-items: center; gap: 8px;
  }
  .call-prompt svg { width: 22px; height: 22px; }
  .phone-main {
    position: absolute;
    left: 60px; top: 724px;
    font-weight: 800;
    font-size: 36px;
    color: var(--navy);
  }
  .trade-list {
    position: absolute;
    left: 60px; top: 770px;
    width: 520px;
    font-size: 17px;
    font-weight: 500;
    line-height: 1.25;
    color: var(--ink);
    text-transform: uppercase;
  }
  .mascot {
    position: absolute;
    left: 590px; top: 500px;
    width: 230px; height: 320px;
    border-radius: 16px;
    background: linear-gradient(180deg, var(--figure-main) 0%, var(--figure-alt) 100%);
  }
  .promise-banner {
    position: absolute;
    left: 28px; top: 836px;
    width: 782px; height: 68px;
    background: var(--navy);
    border-radius: 10px;
    color: var(--paper);
    font-weight: 800;
    font-size: 32px;
    line-height: 68px;
    text-align: center;
  }
  .tear-strip {
    position: absolute;
    left: 0; top: 918px;
    width: 849px; height: 266px;
    display: flex;
  }
  .tear-tab {
    flex: 1;
    border-left: 2px dashed var(--navy);
    display: flex; justify-content: center; align-items: flex-start;
    padding-top: 8px;
  }
  .tear-tab:last-child { border-right: 2px dashed var(--navy); }
  .tear-tab span {
    writing-mode: vertical-rl;
    font-weight: 700;
    font-size: 30px;
    color: var(--navy);
    letter-spacing: 1px;
  }
</style>
</head>
<body>
<main class="leaflet">
  <div class="brand">Harrowgate Property Advisers</div>

  <div class="badge-free">FREE</div>
  <h1 class="headline">TRADESPERSON</h1>
  <p class="subheadline">Recommendation Service</p>

  <p class="trade-range">FOR ANY TRADE A – Z</p>
  <div class="trade-panel">PLUMBER</div>

  <div class="call-prompt">Just Call Us Today
    <svg viewBox="0 0 24 24" aria-hidden="true"><path fill="#1b1f4b" d="M6.6 10.8a15 15 0 0 0 6.6 6.6l2.2-2.2a1 1 0 0 1 1-.25 11.4 11.4 0 0 0 3.6.57 1 1 0 0 1 1 1V20a1 1 0 0 1-1 1A17 17 0 0 1 3 4a1 1 0 0 1 1-1h3.5a1 1 0 0 1 1 1c0 1.25.2 2.45.57 3.57a1 1 0 0 1-.25 1z"/></svg>
  </div>
  <p class="phone-main">01-5528360</p>
  <p class="trade-list">Plumbers, electricians, handymen, carpenters,<br>plasterers, tilers, appliance repairers, cleaners etc</p>

  <div class="mascot" role="img" aria-label="Cartoon plumber in cap and overalls holding a large wrench over his shoulder"></div>

  <div class="promise-banner">WE WILL HELP YOU FIND THE BEST FOR LESS</div>

  <div class="tear-strip">
    <div class="tear-tab"><span>01-5528360</span></div>
    <div class="tear-tab"><span>01-5528360</span></div>
    <div class="tear-tab"><span>01-5528360</span></div>
    <div class="tear-tab"><span>01-5528360</span></div>
    <div class="tear-tab"><span>01-5528360</span></div>
    <div class="tear-tab"><span>01-5528360</span></div>
    <div class="tear-tab"><span>01-5528360</span></div>
    <div class="tear-tab"><span>01-5528360</span></div>
    <div class="tear-tab"><span>01-5528360</span></div>
    <div class="tear-tab"><span>01-5528360</span></div>
    <div class="tear-tab"><span>01-5528360</span></div>
    <div class="tear-tab"><span>01-5528360</span></div>
  </div>
</main>
</body>
</html>
```